Tau Omicron civil engineering orgnization activities flyer

we need flyer design for Tau Omicron civil engineering honor society in Halverton College for mining and industry. the flyer contain the schedule of the expected activity. the design should have a purple color and Tau Omicron Key and logo (you will find them in the attached file) and the design should have something referring to civil engineering

Industry/Entity Type

Education

Colors
6b449b

Requirements
Must have
• Tau Omicron logo, key, motto
Nice to have
• civil engineering samples, purple color

```html
<!DOCTYPE html>
<html lang="en">
<head>
<meta charset="utf-8">
<title>Tau Omicron – Activities Flyer</title>
<link rel="stylesheet" href="https://fonts.googleapis.com/css2?family=Lato:wght@400;700;900&display=swap">
<style>
:root{
  --purple:#6b449b;
  --purple-dark:#3e2463;
  --ink:#2b2b2b;
  --text:#444;
  --muted:#666;
  --paper:#ffffff;
  --section:#ebebec;
  --row-a:#e4e4e6;
  --row-b:#d9d9dc;
  --stage:#e6e6e8;
  --blueprint-a:#c9d2ea;
  --blueprint-b:#5c6fa8;
}
*{margin:0;padding:0;box-sizing:border-box}
html,body{width:1200px;height:806px;overflow:hidden}
body{background:var(--stage);font-family:"Lato",sans-serif;color:var(--text);position:relative}
.flyer{position:absolute;left:335px;top:20px;width:530px;height:766px;background:var(--paper);box-shadow:0 6px 22px rgba(0,0,0,.18);overflow:hidden}

/* header */
.hero{position:absolute;left:0;top:0;width:530px;height:255px}
.hero-visual{position:absolute;left:0;top:0;width:300px;height:255px;background:linear-gradient(135deg,var(--blueprint-a) 0%,#8d9cc8 45%,var(--blueprint-b) 100%)}
.hero-quote{position:absolute;left:18px;top:20px;width:270px;text-align:right;color:#fff;font-size:21px;line-height:1.15;font-weight:400;text-shadow:0 1px 3px rgba(0,0,0,.35)}
.hero-quote b{font-weight:900}
.hero-panel{position:absolute;left:300px;top:0;width:230px;height:255px;background:var(--purple);color:#fff;padding:20px 10px 0 22px}
.brand{display:flex;align-items:center;gap:8px;font-size:20px;font-weight:700;color:#fff;white-space:nowrap}
.brand-dot{width:12px;height:12px;border-radius:50%;background:#fff;flex:none}
.invite{margin-top:58px;font-size:24px;line-height:1.05;font-weight:700;text-transform:uppercase}
.invite .strong{display:block;font-size:29px;font-weight:900;color:var(--purple-dark)}
.invite-details{margin-top:10px;font-size:10px;line-height:1.35;font-weight:700;text-transform:uppercase;color:#efe8f7;white-space:nowrap}

/* schedule */
.schedule{position:absolute;left:0;top:255px;width:530px;height:207px;padding-top:16px}
.section-title{font-size:15px;font-weight:900;color:var(--ink);text-transform:uppercase;letter-spacing:.3px;line-height:1.1}
.schedule .section-title{text-align:center}
.rule{width:34px;height:2px;background:var(--purple);margin:7px auto 11px}
.meetings{width:490px;margin:0 auto;border-collapse:collapse;font-size:9px;color:var(--text)}
.meetings th{background:var(--purple);color:#fff;font-weight:700;font-size:10.5px;text-transform:uppercase;height:17px;padding:0 4px}
.meetings td{height:16px;text-align:center;border-right:1px solid #fff;padding:0 4px}
.meetings tr:nth-child(odd) td{background:var(--row-a)}
.meetings tr:nth-child(even) td{background:var(--row-b)}
.meetings td:last-child{border-right:0}

/* info */
.info{position:absolute;left:0;top:462px;width:530px;height:240px;background:var(--section);display:flex;padding:14px 18px 0 24px;gap:22px;overflow:hidden}
.about{width:272px;font-size:9.2px;line-height:1.32}
.about .section-title{margin-bottom:8px}
.about p{margin-top:7px}
.socials{display:flex;gap:24px;margin-top:11px;font-size:9px;color:var(--purple);font-weight:700}
.social-handle{display:flex;align-items:center;gap:5px}
.social-handle .sq{width:10px;height:10px;background:var(--purple)}
.side{flex:1}
.services{list-style:none;margin-top:10px}
.services li{display:flex;gap:7px;margin-bottom:7px}
.services svg{flex:none;margin-top:1px}
.services strong{display:block;font-size:8.4px;line-height:1.25;color:var(--ink)}
.services span{display:block;font-size:7.2px;line-height:1.3;color:var(--muted)}
.social-title{margin-top:8px}
.social-event{margin-top:8px;font-size:7.3px;line-height:1.35;color:var(--muted)}
.social-event strong{display:block;font-size:8.4px;color:var(--ink)}

/* footer */
.footer{position:absolute;left:0;top:702px;width:530px;height:64px;background:var(--purple);display:flex;align-items:center;padding:0 18px 0 24px;color:#fff}
.footer .brand{width:284px;font-size:22px}
.footer .brand-dot{width:14px;height:14px}
.contact{font-size:7.6px;line-height:1.5;color:#eee6f6}
.contact b{color:#fff}
</style>
</head>
<body>
<main class="flyer">
  <header class="hero">
    <div class="hero-visual" role="img" aria-label="Blue-toned photo of engineering blueprints with a mechanical pencil and compass"></div>
    <p class="hero-quote">If you <b>help someone,</b><br>it costs <b>you</b> nothing!</p>
    <div class="hero-panel">
      <div class="brand"><span class="brand-dot"></span>Tau Omicron</div>
      <h1 class="invite">Invitation<span class="strong">For Dinner</span></h1>
      <p class="invite-details">12/12/2015, 6:30PM, Marlowe's -<br>410 North Ashgrove Street,<br>Halverton</p>
    </div>
  </header>

  <section class="schedule">
    <h2 class="section-title">Meeting Schedule</h2>
    <div class="rule"></div>
    <table class="meetings">
      <thead><tr><th>Meeting No.</th><th>Date</th><th>Time</th><th>Location</th><th>Name</th><th>Company</th></tr></thead>
      <tbody>
        <tr><td>01</td><td>9/8/2015</td><td>7 PM</td><td>BCH 124</td><td>Dr. Whitcombe</td><td></td></tr>
        <tr><td>02</td><td>9/22/2015</td><td>7 PM</td><td>BCH 124</td><td>Dell Farrow</td><td>Metro Waterworks</td></tr>
        <tr><td>03</td><td>10/6/2015</td><td>7 PM</td><td>BCH 124</td><td>Owen Lassiter</td><td>Ft. Ridgemont</td></tr>
        <tr><td>04</td><td>10/20/2015</td><td>7 PM</td><td>BCH 124</td><td>Reese Calloway</td><td>Norvale Inc.</td></tr>
        <tr><td>05</td><td>11/3/2015</td><td>7 PM</td><td>BCH 124</td><td>Scavenger Hunt</td><td>Social</td></tr>
        <tr><td>06</td><td>11/17/2015</td><td>7 PM</td><td>BCH 124</td><td>Nomination/Ben Harlan</td><td>Grant Mercer</td></tr>
        <tr><td>07</td><td>12/1/2015</td><td>7 PM</td><td>BCH 124</td><td>Elections</td><td></td></tr>
      </tbody>
    </table>
  </section>

  <section class="info">
    <div class="about">
      <h2 class="section-title">About Us</h2>
      <p>Tau Omicron is the National Civil Engineering Honor Society in the United States. We honor engineering students who have exemplified the principles of "Scholarship, Character, Practicality, and Sociability" in the civil engineering profession.</p>
      <p>Tau Omicron retains as its motto the Greek letters Tau Delta Omicron, which formed the name of the junior honor society founded in 1922 at Halverton College for mining and industry and which is one of the roots of Tau Omicron.</p>
      <p>Members of Tau Omicron are considered top graduates and are highly sought by civil engineering employers.</p>
      <div class="socials">
        <span class="social-handle"><span class="sq"></span>TauOmicronNational</span>
        <span class="social-handle"><span class="sq"></span>TauOmicronNational</span>
      </div>
    </div>
    <div class="side">
      <h2 class="section-title">Services</h2>
      <ul class="services">
        <li><svg width="10" height="10" viewBox="0 0 10 10"><circle cx="5" cy="5" r="4.3" fill="none" stroke="#333" stroke-width="1"/><path d="M2.8 5.1l1.5 1.5 3-3" fill="none" stroke="#333" stroke-width="1.1"/></svg>
          <div><strong>Fenwick Conservation Area Service Day</strong><span>Saturday, Oct 24, 11 am / Fenwick Conservation Area, Halverton, United States</span></div></li>
        <li><svg width="10" height="10" viewBox="0 0 10 10"><circle cx="5" cy="5" r="4.3" fill="none" stroke="#333" stroke-width="1"/><path d="M2.8 5.1l1.5 1.5 3-3" fill="none" stroke="#333" stroke-width="1.1"/></svg>
          <div><strong>Community Partnership Service Day</strong><span>Saturday, Nov 7, 11 am / The Neighbor Aid Resale Shop, 2200 N Alder Ave, Halverton, United States</span></div></li>
        <li><svg width="10" height="10" viewBox="0 0 10 10"><circle cx="5" cy="5" r="4.3" fill="none" stroke="#333" stroke-width="1"/><path d="M2.8 5.1l1.5 1.5 3-3" fill="none" stroke="#333" stroke-width="1.1"/></svg>
          <div><strong>Tri County Animal Shelter Volunteer Day</strong><span>Thursday, Nov 12, 12 pm / Tri County Animal Shelter, 318 E Linden St, Halverton, United States</span></div></li>
      </ul>
      <h2 class="section-title social-title">Social</h2>
      <p class="social-event"><strong>Tau Omicron Smoker</strong>Bowling/Strikeline Lanes (1120 Quarry Road), Wednesday, October 28th - 9:00 PM<br>Plaque Signing/ When: December 8th - the Zone</p>
    </div>
  </section>

  <footer class="footer">
    <div class="brand"><span class="brand-dot"></span>Tau Omicron</div>
    <p class="contact">Room 214, Brandt Hall, Halverton 40112-0208.<br>Phone: <b>555.014.0270</b> | Email: <b>office@tau-omicron.org</b><br>Website: <b>www.tau-omicron.org</b></p>
  </footer>
</main>
</body>
</html>
```